Medical group practice

We need a flyer design incorporating the three doctors in the practice, there is a general practitioner, ophthalmologist and an obstetrician & Gynaecologist. see the attached file for the concept. will leave the colour design up to you

Target Market(s)

general public

Industry/Entity Type

Health Care

Colors

Designer to choose colors to be used in the design.

Requirements
Must have
• logos included in attachement

```html
<!DOCTYPE html>
<html lang="en">
<head>
<meta charset="utf-8">
<title>Coraline Medical Flyer</title>
<link rel="stylesheet" href="https://fonts.googleapis.com/css2?family=Montserrat:wght@600;700&family=PT+Sans:wght@400;700&display=swap">
<style>
:root{
  --stage:#454545;
  --red:#c8141e;
  --red-dark:#a50d15;
  --ink:#111;
  --body:#222;
  --grey:#a7a9ac;
  --paper:#ffffff;
  --paper-fade:#e9e9ea;
  --eye-purple:#7b1a85;
  --logo-blue:#1a7fb8;
}
*{margin:0;padding:0;box-sizing:border-box}
html,body{width:1200px;height:1200px;overflow:hidden;background:var(--stage)}
.flyer{position:absolute;left:176px;top:0;width:848px;height:1200px;overflow:hidden;
  background:linear-gradient(180deg,var(--paper) 0%,var(--paper) 40%,var(--paper-fade) 100%);
  font-family:"PT Sans",Arial,sans-serif;color:var(--body)}
.backdrop{position:absolute;left:0;top:0}
.abs{position:absolute;white-space:nowrap}
.brand{left:50px;top:36px;font-family:"Montserrat",Arial,sans-serif;font-weight:700;font-size:41px;color:var(--red);letter-spacing:.5px}
.tagline{left:50px;top:88px;font-family:"Montserrat",Arial,sans-serif;font-weight:600;font-size:41px;line-height:53px;color:var(--ink)}
.practice-name{font-family:"PT Sans",Arial,sans-serif;font-weight:700;font-size:13px;color:var(--logo-blue);letter-spacing:.5px}
.practice-mark{display:inline-block;width:12px;height:12px;border-radius:50%;background:var(--logo-blue);vertical-align:-1px;margin-right:6px}
.doctor-name{font-family:"Montserrat",Arial,sans-serif;font-weight:700;font-size:22px;color:var(--red)}
.doctor-name small{font-size:15px}
.credentials{font-family:"Montserrat",Arial,sans-serif;font-weight:700;font-size:16px;color:var(--red)}
.specialty{font-weight:400;font-size:21px;color:var(--ink)}
.services{font-size:14.3px;line-height:18.7px;color:var(--body);white-space:normal;width:400px}
.services u{font-weight:700}
.contact{font-size:15.5px;color:var(--ink)}
.contact svg{vertical-align:-1px;margin-right:3px}
.contact .gap{display:inline-block;width:14px}
.hours-title{right:33px;top:745px;font-family:"Montserrat",Arial,sans-serif;font-weight:700;font-size:33px;color:var(--red);text-align:right}
.hours{right:33px;top:784px;font-weight:700;font-size:23px;line-height:31px;color:var(--ink);text-align:right}
.footer{position:absolute;left:0;top:1168px;width:848px;height:32px;background:linear-gradient(90deg,var(--red-dark),var(--red),var(--red-dark));color:#fff;font-weight:700;font-size:13.5px}
.footer span{position:absolute;top:8px}
.footer svg{vertical-align:-2px;margin-right:6px}
.corner-mark{left:610px;top:1000px;text-align:center;font-family:"Montserrat",Arial,sans-serif;font-weight:700;font-size:18px;color:var(--red)}
.corner-mark .dot{display:block;margin:0 auto 10px;width:70px;height:70px;border-radius:50%;background:var(--red)}
</style>
</head>
<body>
<main class="flyer">
  <svg class="backdrop" width="848" height="1200" viewBox="0 0 848 1200">
    <defs>
      <linearGradient id="heroTone" x1="0" y1="0" x2="1" y2="0">
        <stop offset="0" stop-color="#ffffff"/>
        <stop offset="0.45" stop-color="#e3ecf5"/>
        <stop offset="1" stop-color="#d7e3ef"/>
      </linearGradient>
      <linearGradient id="teamTone" x1="0" y1="0" x2="0" y2="1">
        <stop offset="0" stop-color="#eef2f6"/>
        <stop offset="1" stop-color="#b9cde0"/>
      </linearGradient>
      <linearGradient id="swoosh" x1="0" y1="0" x2="1" y2="0">
        <stop offset="0" stop-color="#d3151f"/>
        <stop offset="0.6" stop-color="#e31b23"/>
        <stop offset="1" stop-color="#9c0d14"/>
      </linearGradient>
    </defs>
    <rect role="img" aria-label="Photo of a smiling female doctor with a stethoscope, colleagues blurred behind" x="300" y="0" width="548" height="480" fill="url(#heroTone)"/>
    <path d="M0 135 C120 330 300 420 560 430 L848 430 L848 520 L0 520 Z" fill="#f2f2f3"/>
    <path d="M0 135 C110 320 290 410 560 430 C520 440 220 400 0 250 Z" fill="var(--grey)"/>
    <path d="M0 200 C130 370 330 440 560 430 L700 435 C520 460 200 430 0 300 Z" fill="url(#swoosh)"/>
    <circle cx="680" cy="537" r="166" fill="var(--red)"/>
    <circle cx="680" cy="537" r="156" fill="#fff"/>
    <circle role="img" aria-label="Photo of the practice team of four doctors" cx="680" cy="537" r="150" fill="url(#teamTone)"/>
  </svg>

  <div class="abs brand">CORALINE MEDICAL</div>
  <div class="abs tagline">Your Health is our<br>PRIORITY</div>

  <div class="abs practice-name" style="left:50px;top:434px"><span class="practice-mark"></span>HARBOUR LANE FAMILY PRACTICE</div>
  <div class="abs doctor-name" style="left:30px;top:458px">Dr. Elton Marsh, <small>MD.</small></div>
  <div class="abs specialty" style="left:30px;top:484px">General Practitioner</div>
  <div class="abs services" style="left:30px;top:511px">General Checks, &nbsp;Annual Check ups, Wound Care/Dressings, Incision &amp; Drainage, Suturing lacerations, Pain Injections, Glucose checks, Foreign Body Removal.</div>
  <div class="abs contact" style="left:30px;top:581px"><svg width="13" height="10" viewBox="0 0 13 10"><rect width="13" height="10" fill="var(--red)"/><path d="M0 0 L6.5 5.5 L13 0" stroke="#fff" fill="none"/></svg>elton.marsh.doc@example.com<span class="gap"></span><svg width="11" height="11" viewBox="0 0 24 24"><path d="M6.6 10.8a15 15 0 006.6 6.6l2.2-2.2a1 1 0 011-.25 11 11 0 003.6.6 1 1 0 011 1V20a1 1 0 01-1 1A17 17 0 013 4a1 1 0 011-1h3.5a1 1 0 011 1 11 11 0 00.6 3.6 1 1 0 01-.25 1z" fill="var(--red)"/></svg>(555) 214 7730</div>

  <div class="abs practice-name" style="left:30px;top:695px;color:var(--eye-purple)"><span class="practice-mark" style="background:var(--eye-purple)"></span>Clearview Eye Service</div>
  <div class="abs doctor-name" style="left:30px;top:721px">Dr. Lucia R. Benitez, <small>MD.</small></div>
  <div class="abs specialty" style="left:30px;top:746px">Surgeon Ophthalmologist</div>
  <div class="abs services" style="left:30px;top:777px">Eyes disease examination, Surgery of Pterygium, Cataract, Glaucoma, Emergency, Conjunctivitis, Traumatism, Foreign body and more.</div>
  <div class="abs contact" style="left:30px;top:839px"><svg width="13" height="10" viewBox="0 0 13 10"><rect width="13" height="10" fill="var(--red)"/><path d="M0 0 L6.5 5.5 L13 0" stroke="#fff" fill="none"/></svg>lucia.eyes@example.com<span class="gap"></span><svg width="11" height="11" viewBox="0 0 24 24"><path d="M6.6 10.8a15 15 0 006.6 6.6l2.2-2.2a1 1 0 011-.25 11 11 0 003.6.6 1 1 0 011 1V20a1 1 0 01-1 1A17 17 0 013 4a1 1 0 011-1h3.5a1 1 0 011 1 11 11 0 00.6 3.6 1 1 0 01-.25 1z" fill="var(--red)"/></svg>(555) 318 4092</div>

  <div class="abs" style="left:70px;top:900px;width:40px;height:40px;border-radius:50%;background:var(--logo-blue)"></div>
  <div class="abs doctor-name" style="left:30px;top:952px">Dr. Keon Ashby,</div>
  <div class="abs credentials" style="left:30px;top:978px">BMedSci, MBBS, DM (O&amp;G), FACOG</div>
  <div class="abs specialty" style="left:30px;top:1001px">Obstetrician &amp; Gynaecologist</div>
  <div class="abs services" style="left:30px;top:1032px"><u>Obstetrics:</u>Prenatal Care, Delivery, Postnatal checks, High Risk pregnancy<br><u>Gynaecology:</u> Pap smears, Abnormal vaginal bleeding, Fibroids, Colposcopy, Family planning, Infertility, Cancer screening, And More….</div>
  <div class="abs contact" style="left:30px;top:1136px"><svg width="13" height="10" viewBox="0 0 13 10"><rect width="13" height="10" fill="var(--red)"/><path d="M0 0 L6.5 5.5 L13 0" stroke="#fff" fill="none"/></svg>dr.ashby@example.com<span class="gap"></span><svg width="11" height="11" viewBox="0 0 24 24"><path d="M6.6 10.8a15 15 0 006.6 6.6l2.2-2.2a1 1 0 011-.25 11 11 0 003.6.6 1 1 0 011 1V20a1 1 0 01-1 1A17 17 0 013 4a1 1 0 011-1h3.5a1 1 0 011 1 11 11 0 00.6 3.6 1 1 0 01-.25 1z" fill="var(--red)"/></svg>(555) 462 1180 / (555) 509 7743</div>

  <div class="abs hours-title">Opening hours</div>
  <div class="abs hours">Monday – Friday: 9am-6pm<br>Saturday: 10am – 5pm</div>

  <div class="abs corner-mark"><span class="dot"></span>CORALINE MEDICAL</div>

  <footer class="footer">
    <span style="left:106px"><svg width="12" height="15" viewBox="0 0 24 30"><path d="M12 0a12 12 0 0112 12c0 9-12 18-12 18S0 21 0 12A12 12 0 0112 0z" fill="#fff"/><circle cx="12" cy="12" r="4.5" fill="var(--red)"/></svg>42 Harbour Road, Port Verano</span>
    <span style="left:466px"><svg width="15" height="15" viewBox="0 0 24 24"><path d="M6.6 10.8a15 15 0 006.6 6.6l2.2-2.2a1 1 0 011-.25 11 11 0 003.6.6 1 1 0 011 1V20a1 1 0 01-1 1A17 17 0 013 4a1 1 0 011-1h3.5a1 1 0 011 1 11 11 0 00.6 3.6 1 1 0 01-.25 1z" fill="#fff"/></svg>(555) 410 2280 / 2281</span>
  </footer>
</main>
</body>
</html>
```